Redesign Of Flower Delivery Subscription Service Website

I need a revamped website of www.petal-rush.com

Please revamp current design using same content....

Target Market(s)

people who buy flowers. Brides, wedding planners, wedding photographer, married man, boyfriend, etc.

Industry/Entity Type

Florist

Number of Pages Required

5+ page

Colors

Designer to choose colors to be used in the design.

Requirements
Must have
• I need a revamped website of www.petal-rush.com
• Please revamp current design using same content....
Nice to have
Should not have

```html
<!DOCTYPE html>
<html lang="en">
<head>
<meta charset="utf-8">
<title>PetalRush — Monthly Flower Delivery</title>
<link rel="stylesheet" href="https://fonts.googleapis.com/css2?family=Libre+Baskerville:wght@400;700&family=Montserrat:wght@400;500;600;700&display=swap">
<style>
:root{
  --green:#8cc63f;
  --green-dark:#6fa82a;
  --orange:#f7a823;
  --ink:#222;
  --body:#444;
  --muted:#888;
  --grey-band:#f1f1ef;
  --panel:#4b4644;
  --white:#fff;
  --line:#ddd;
}
*{box-sizing:border-box;margin:0;padding:0}
html,body{width:698px;height:1200px;overflow:hidden;background:var(--white)}
body{position:relative;font-family:"Montserrat",sans-serif;color:var(--body)}
.abs{position:absolute}
.serif{font-family:"Libre Baskerville",serif}

/* header */
.brand{left:94px;top:16px;display:flex;align-items:center;gap:6px}
.brand-mark{width:14px;height:14px;border-radius:50%;background:var(--green)}
.brand-name{font-size:19px;font-weight:600;color:var(--green-dark);letter-spacing:.5px}
.info{top:17px;font-size:6.5px;color:var(--ink)}
.info-label{color:var(--green);font-weight:600;margin-bottom:4px}
.info-value{display:flex;align-items:center;gap:4px}
.info-phone .info-value{font-size:8px;font-weight:600}
.hbtn{top:18px;height:19px;font-size:5.5px;font-weight:700;color:var(--white);display:flex;align-items:center;justify-content:center;gap:3px;border-radius:2px}
.hbtn-buy{left:500px;width:60px;background:var(--green)}
.hbtn-login{left:562px;width:42px;background:var(--orange)}

.nav{left:0;top:56px;width:698px;height:22px;background:var(--green)}
.nav ul{list-style:none;display:flex;position:absolute;left:94px;top:0;height:22px}
.nav li{font-size:5.4px;font-weight:600;color:var(--white);padding:0 10px;line-height:22px;border-right:1px solid rgba(255,255,255,.35)}
.nav li:first-child{border-left:1px solid rgba(255,255,255,.35)}

/* hero */
.hero{left:0;top:78px;width:698px;height:246px;background:linear-gradient(180deg,#d9dfd6 0%,#c4cfbc 45%,#cfd6dc 78%,#a9b8d6 100%)}
.offer{left:394px;top:102px;width:172px;height:182px;background:var(--panel);opacity:.96;border-radius:24px 0 24px 0;color:var(--white);text-align:center}
.offer-inner{position:absolute;inset:5px;border:1px solid rgba(255,255,255,.55);border-radius:20px 0 20px 0}
.offer h2{font-size:13px;font-weight:400;margin-top:30px;letter-spacing:.5px}
.offer p{font-family:"Libre Baskerville",serif;font-size:7.2px;font-weight:700;line-height:10px;margin-top:9px}
.offer .price-lead{font-weight:400;margin-top:14px}
.offer .price{font-size:11px;margin-top:0}
.offer .price small{font-size:7px}
.tags{display:flex;justify-content:center;gap:3px;margin-top:10px}
.tag{font-size:4.2px;font-weight:700;padding:3px 6px;border-radius:6px;background:var(--green)}
.tag.alt{background:var(--orange)}

/* steps */
.step{top:300px;width:150px;text-align:center}
.step-ring{width:80px;height:44px;margin:0 auto;position:relative}
.step-icon{position:absolute;left:8px;top:6px;width:64px;height:64px;border-radius:50%;display:flex;align-items:center;justify-content:center}
.step h3{font-size:6.4px;font-weight:700;color:var(--ink);margin-top:42px}
.step p{font-size:5.5px;line-height:10.4px;margin-top:7px}
.step p+p{margin-top:6px}
.arrow{top:340px}

/* intro band */
.band{left:0;top:494px;width:698px;height:261px;background:var(--grey-band)}
.intro-title{left:94px;top:518px;width:380px;font-size:9px;font-weight:700;letter-spacing:.6px;line-height:13px;color:var(--green)}
.intro-title span{color:var(--orange)}
.intro-text{left:94px;top:546px;width:380px;font-size:5.1px;line-height:10.5px;color:var(--ink)}
.col{top:622px;width:124px;height:114px;text-align:center}
.col h4{font-size:5.5px;font-weight:600;line-height:10.5px;color:var(--orange)}
.col p{font-size:5.1px;line-height:10.4px;color:var(--ink);margin-top:8px}
.col a{position:absolute;left:0;right:0;bottom:0;display:block;font-size:5.4px;font-weight:700;color:var(--ink);text-decoration:none}

.signin{left:486px;top:494px;width:119px;height:261px;background:var(--green);color:var(--white);text-align:center;padding:0 8px}
.signin .hello{font-size:7px;margin-top:24px}
.signin .title{font-size:13px;margin-top:2px;letter-spacing:.5px}
.field{height:20px;background:var(--white);border:1px solid #e3e3e3;margin-top:6px;font-size:4.8px;color:var(--muted);text-align:left;padding-left:7px;line-height:19px}
.signin .title+.field{margin-top:10px}
.obtn{height:20px;background:var(--orange);border-radius:2px;font-size:6.5px;font-weight:700;line-height:20px;margin-top:7px;color:var(--white)}
.forgot{font-size:4.2px;margin-top:7px}
.rule{border-top:1px solid rgba(255,255,255,.6);margin:10px 0 0}
.signin .notm{font-size:7px;margin-top:13px}
.signin .join{font-size:13px;margin-top:3px}
.signin .sub{font-size:5.4px;line-height:8.5px;margin-top:4px}

/* occasion tiles */
.tile{color:var(--white);display:flex;align-items:center;justify-content:center;flex-direction:column}
.tile h3{font-family:"Libre Baskerville",serif;font-size:12px;font-weight:400;letter-spacing:1.6px}
.tile span{font-size:6.4px;letter-spacing:.6px;padding:6px 6px 3px;border-top:1px solid rgba(255,255,255,.8);border-bottom:1px solid rgba(255,255,255,.8);margin-top:5px}
.t-anniv{left:94px;top:782px;width:161px;height:109px;background:linear-gradient(135deg,#8a8a7a,#b5a48c)}
.t-birth{left:94px;top:900px;width:161px;height:154px;background:linear-gradient(135deg,#6f7370,#9c9993)}
.t-deliv{left:262px;top:782px;width:173px;height:272px;background:linear-gradient(180deg,#5c6068,#6b5b5f 60%,#7c4c4e)}
.t-deliv h3{font-size:11px;letter-spacing:1.2px}
.t-deliv .frame{position:absolute;left:16px;top:14px;right:16px;bottom:14px;border:3px solid var(--white)}
.t-valen{left:442px;top:782px;width:162px;height:154px;background:linear-gradient(135deg,#7c6c62,#a4978c)}
.t-mother{left:442px;top:944px;width:162px;height:110px;background:linear-gradient(135deg,#8b7d72,#b08f7a)}

/* footer */
.fcol{top:1079px}
.fcol h5{font-size:6.4px;font-weight:700;color:var(--ink);padding-bottom:5px;border-bottom:1px dotted #999;width:74px}
.fcol ul{list-style:none;margin-top:10px}
.fcol li{font-size:5.3px;color:var(--ink);line-height:10.4px}
.news h5{width:130px}
.news-field{width:130px;height:21px;border:1px solid var(--line);margin-top:11px;display:flex;justify-content:space-between;align-items:center;padding:0 8px;font-size:4.4px;color:#aaa}
.news-field b{font-size:5.4px;color:var(--ink);letter-spacing:.5px}
.follow{display:flex;align-items:center;gap:5px;margin-top:10px;font-size:6.2px;font-weight:700;color:var(--ink)}
.dot{width:7px;height:7px;border-radius:50%;background:#aab}
.dot.g{background:var(--green)}
.contact li{display:flex;gap:5px;align-items:flex-start;margin-bottom:4px;font-size:5.8px;line-height:8.5px}
.contact li svg{flex:none;margin-top:1px}
.foot-rule{left:94px;top:1170px;width:511px;border-top:1px solid var(--line)}
.copy{left:0;top:1181px;width:698px;text-align:center;font-size:4.6px;color:var(--ink)}
</style>
</head>
<body>

<header>
  <div class="abs brand"><span class="brand-mark"></span><span class="brand-name">PetalRush</span></div>

  <div class="abs info" style="left:250px">
    <div class="info-label">Our Address:</div>
    <div class="info-value">
      <svg width="6" height="7" viewBox="0 0 12 14"><path d="M6 0a5 5 0 0 0-5 5c0 4 5 9 5 9s5-5 5-9a5 5 0 0 0-5-5zm0 7a2 2 0 1 1 0-4 2 2 0 0 1 0 4z" fill="#8cc63f"/></svg>
      1480 Marigold Avenue, Lakeview CA 90412
    </div>
  </div>
  <div class="abs info info-phone" style="left:424px">
    <div class="info-label">Phone</div>
    <div class="info-value">
      <svg width="7" height="7" viewBox="0 0 14 14"><path d="M3 1l2 3-1.5 1.5a8 8 0 0 0 5 5L10 9l3 2-1 2.5C6 14 0 8 .5 2z" fill="none" stroke="#8cc63f" stroke-width="1.3"/></svg>
      555-014-2290
    </div>
  </div>
  <div class="abs hbtn hbtn-buy">
    <svg width="7" height="6" viewBox="0 0 14 12"><path d="M0 1h3l2 7h7l2-5H4" fill="none" stroke="#fff" stroke-width="1.5"/><circle cx="6" cy="11" r="1" fill="#fff"/><circle cx="11" cy="11" r="1" fill="#fff"/></svg>
    BUY NOW
  </div>
  <div class="abs hbtn hbtn-login">
    <svg width="5" height="6" viewBox="0 0 10 12"><circle cx="5" cy="3" r="2.5" fill="#fff"/><path d="M0 12a5 5 0 0 1 10 0z" fill="#fff"/></svg>
    LOGIN
  </div>
</header>

<nav class="abs nav">
  <ul>
    <li>HOME</li><li>HOW IT WORKS</li><li>CORPORATE ARRANGEMENTS</li><li>EVENTS</li><li>WEDDINGS</li><li>DELIVERY AREAS</li><li>FRANCHISE</li><li>CONTACT US</li>
  </ul>
</nav>

<section class="abs hero" role="img" aria-label="Photo of a colourful bouquet in a blue vase on a table before a bright window"></section>

<div class="abs offer">
  <div class="offer-inner"></div>
  <h2 class="serif">ALWAYS FRESH</h2>
  <p>Beautiful Flower Arrangements<br>Delivered Monthly</p>
  <p class="price-lead">Now only</p>
  <p class="price">$69.95/MTH <small>($100 value)</small></p>
  <div class="tags"><span class="tag">FREE VASE</span><span class="tag alt">FREE DELIVERY</span><span class="tag">FREE UPGRADE</span></div>
</div>

<section class="how">
  <div class="abs step" style="left:99px">
    <div class="step-ring"><div class="step-icon" style="background:var(--green)">
      <svg width="30" height="24" viewBox="0 0 30 24" fill="none" stroke="#fff" stroke-width="1.6"><rect x="1" y="1" width="24" height="18" rx="1"/><path d="M5 6h8M5 10h14M5 14h6"/><path d="M18 17l3 3 7-7"/></svg>
    </div></div>
    <h3>SET IT AND FORGET IT</h3>
    <p>PetalRush is a "SET IT and FORGET IT"<br>subscription based flower delivery service.</p>
    <p>For an Amazing price PetalRush will hand<br>deliver a gorgeous arrangement directly to<br>anyone you want every month without you<br>having to worry about it.</p>
  </div>
  <div class="abs step" style="left:271px">
    <div class="step-ring"><div class="step-icon" style="background:var(--orange)">
      <svg width="28" height="26" viewBox="0 0 28 26" fill="none" stroke="#fff" stroke-width="1.5"><rect x="2" y="4" width="24" height="20" rx="1"/><path d="M2 10h24M8 1v6M20 1v6M8 14h3M13 14h3M18 14h3M8 18h3M13 18h3M18 18h3"/></svg>
    </div></div>
    <h3>BUT NEVER FORGET AGAIN</h3>
    <p>When setting up your account, you can<br>choose exact delivery dates for the months<br>that have special days such as your<br>Anniversary, Birthday, Valentines Day and<br>Mothers Day. You might forget but we won't,<br>we have got ya covered!</p>
  </div>
  <div class="abs step" style="left:446px">
    <div class="step-ring"><div class="step-icon" style="background:var(--green)">
      <svg width="24" height="28" viewBox="0 0 24 28" fill="none" stroke="#fff" stroke-width="1.5"><circle cx="12" cy="9" r="7"/><path d="M8 16l4 11 4-11"/></svg>
    </div></div>
    <h3>MAKING SOMEONE'S DAY BETTER</h3>
    <p>Be the hero in that special someone's<br>life each and every month.</p>
    <p>It feels good to make a difference in<br>your loved ones day.</p>
  </div>
  <svg class="abs arrow" style="left:250px" width="28" height="10" viewBox="0 0 28 10"><path d="M1 7q12-6 25 0M22 3l4 4-5 1" fill="none" stroke="#333" stroke-width="1"/></svg>
  <svg class="abs arrow" style="left:422px" width="28" height="10" viewBox="0 0 28 10"><path d="M1 5q12 6 25-2M21 1l5 2-3 4" fill="none" stroke="#333" stroke-width="1"/></svg>
</section>

<section class="abs band"></section>
<h2 class="abs intro-title serif">MONTHLY SUBSCRIPTION BASED FLOWER DELIVERY SERVICE IN LAKEVIEW – <span>CA BY OUR FLORIST SHOP</span></h2>
<p class="abs intro-text">Every moment of life could be cherished perfectly......IF you choose wisely. To make your day more treasured, remember that flowers are the smartest choice when delivered through our monthly PetalRush subscription based delivery service. Our online subscription-based flower delivery service can help you pamper, cherish and make an everlasting impression on the minds of your loved ones with a doorstep delivery of exquisitely hand-designed floral arrangements. Our online subscription service features both standard and personalized services to help you choose from an assortment of classic and contemporary floral arrangements. It is your chance to setup a weekly, monthly, or quarterly subscription, so we can deliver the most exotic collections of hand-decorated flowers that you and your loved ones will cherish.</p>

<div class="abs col" style="left:91px">
  <h4>Get Yourself Subscribed And Claim<br>Discounts On Big Orders!</h4>
  <p>Let's not forget a single day in which you can make your loved ones feel special. Whether it's your anniversary or a birthday in your family, you must always go an extra mile to show "how much I care about you." Nothing can compare to your show of love, or compliment the joy of your loved</p>
  <a>READ MORE</a>
</div>
<div class="abs col" style="left:222px">
  <h4>Exotic Flowers Garnished With Special<br>Hues To Compliment Your Loved Ones</h4>
  <p>PetalRush offers on time subscription based service that is risk free, trouble free and affordable at the same time. We offer the most trusted and delightful flower delivery service in Lakeview, and are designed to deliver your desired floral arrangements within your requested days and times.</p>
  <a>READ MORE</a>
</div>
<div class="abs col" style="left:353px">
  <h4>Standard And Personalized Flower<br>Arrangements For Special Occasions</h4>
  <p>Get love and adulation by gifting flowers to your loved ones on those special occasions. Whether it's formal, personal or your love for your family, just follow the subscription criteria and get your hands on the most valuable service for all kinds of events, occasions and parties.</p>
  <a>READ MORE</a>
</div>

<aside class="abs signin">
  <p class="hello serif">WELCOME TO</p>
  <p class="title serif">PETAL RUSH!</p>
  <div class="field">Email Address</div>
  <div class="field">Password</div>
  <div class="obtn">SIGN IN NOW!</div>
  <p class="forgot">Forgot your Registered Email?</p>
  <div class="rule"></div>
  <p class="notm serif">NOT A MEMBER?</p>
  <p class="join serif">JOIN NOW!</p>
  <p class="sub">Click to register here and get a<br>offers &amp; discounts</p>
  <div class="obtn" style="margin-top:12px">JOIN NOW!</div>
</aside>

<section class="occasions">
  <div class="abs tile t-anniv" role="img" aria-label="Photo of an older couple sharing flowers"><h3>ANNIVERSARY</h3><span>BOOK NOW</span></div>
  <div class="abs tile t-birth" role="img" aria-label="Photo of a couple celebrating a birthday with flowers"><h3>BRITHDAY</h3><span>BOOK NOW</span></div>
  <div class="abs tile t-deliv" role="img" aria-label="Photo of a delivery man holding a bouquet"><div class="frame"></div><h3>DELIVERY AREAS</h3><span>CLICK HERE</span></div>
  <div class="abs tile t-valen" role="img" aria-label="Photo of a couple on Valentines Day"><h3>VALENTINES DAY</h3><span>BOOK NOW</span></div>
  <div class="abs tile t-mother" role="img" aria-label="Photo of a child giving flowers to her mother"><h3>MOTHERS DAY</h3><span>BOOK NOW</span></div>
</section>

<footer>
  <div class="abs fcol" style="left:94px">
    <h5>INFORMATION</h5>
    <ul><li>Home</li><li>About Us</li><li>Delivery</li><li>Policy Disclaimer</li></ul>
  </div>
  <div class="abs fcol" style="left:199px">
    <h5>MY ACCOUNT</h5>
    <ul><li>Contact</li><li>FAQs</li><li>Terms &amp; Conditions</li><li>Privacy Policy</li></ul>
  </div>
  <div class="abs fcol news" style="left:312px">
    <h5>OUR NEWSLETTER</h5>
    <div class="news-field">Your Email Address <b>SEND</b></div>
    <div class="follow">FOLLOW US <span class="dot g"></span><span class="dot"></span><span class="dot"></span><span class="dot"></span></div>
  </div>
  <div class="abs fcol contact" style="left:486px">
    <h5>CONTACT</h5>
    <ul>
      <li><svg width="6" height="7" viewBox="0 0 12 14"><path d="M6 0a5 5 0 0 0-5 5c0 4 5 9 5 9s5-5 5-9a5 5 0 0 0-5-5zm0 7a2 2 0 1 1 0-4 2 2 0 0 1 0 4z" fill="#8cc63f"/></svg><span>1480 Marigold Avenue,<br>Lakeview CA 90412</span></li>
      <li><svg width="7" height="7" viewBox="0 0 14 14"><path d="M3 1l2 3-1.5 1.5a8 8 0 0 0 5 5L10 9l3 2-1 2.5C6 14 0 8 .5 2z" fill="none" stroke="#8cc63f" stroke-width="1.3"/></svg><span>555-014-2290</span></li>
      <li><svg width="7" height="6" viewBox="0 0 14 10"><rect x=".5" y=".5" width="13" height="9" fill="none" stroke="#8cc63f"/><path d="M.5.5L7 6l6.5-5.5" fill="none" stroke="#8cc63f"/></svg><span>support@petal-rush.com</span></li>
    </ul>
  </div>
  <div class="abs foot-rule"></div>
  <p class="abs copy">Copyright © 2018 - PetalRush. All Right Reserved.</p>
</footer>

</body>
</html>
```